Zielgruppe
Wir eröffnen einen neune Onlineshop rund um das Thema Gartengeräte, im Sinne von Schläuchen, Schlauchwagen, Gartenbewässerung, Blumenkästen und Co.
Aufgabenstellung
Wir benötigen für diesen Shop ein komplettes Design ( Header,Footer, Menü, Detailansicht, Buttons) welches wir nachher in unseren Kerbel Shop einbinden.
Das Template wird von uns erstellt.
Die farbliche Gestaltung sollte zum Thema passen, hier dürfen also gerne Blau und Grüntöne verwendet werden.
Es soll kein klassisches 3 Spaltenlayout sein, gerne würden wir mit einem 2 Spaltenlayout arbeiten, links mit der Kategoriespalte und dann eine große Produkt und Inhaltsspalte
Der Shop wird den Namen minaru tragen.

```html
<!DOCTYPE html>
<html lang="en">
<head>
<meta charset="utf-8">
<title>Minaru – Garden Shop</title>
<link href="https://fonts.googleapis.com/css2?family=Ubuntu:wght@300;400;500;700&display=swap" rel="stylesheet">
<style>
:root{
  --green:#8cc63f;
  --green-text:#7dbb2c;
  --green-pale:#f2f8e4;
  --footer-bg:#eef5dc;
  --blue:#3e8fd1;
  --dark:#3a3a3a;
  --text:#444;
  --muted:#888;
  --line:#dcdcdc;
}
*{box-sizing:border-box;margin:0;padding:0}
html,body{width:710px;height:1200px;overflow:hidden;background:#fff}
body{font-family:'Ubuntu',sans-serif;color:var(--text)}
.page{position:absolute;left:0;top:0;width:1200px;height:2028px;transform:scale(.591667);transform-origin:0 0}
.abs{position:absolute}
.logo{left:60px;top:10px;font-size:56px;font-weight:400;color:var(--green);letter-spacing:1px}
.phone{left:603px;top:30px;font-size:24px;color:var(--green-text);display:flex;align-items:center;gap:6px}
.currency{left:877px;top:36px;font-size:12px;color:var(--muted)}
.currency-select{left:950px;top:33px;width:108px;height:19px;border:1px solid #ccc;font-size:10px;color:var(--muted);padding:3px 6px}
.currency-select::after{content:"▼";position:absolute;right:8px;top:3px;font-size:8px;color:#aaa}
.flag{top:34px;width:20px;height:14px}
.header-rule{left:305px;top:70px;width:835px;height:1px;background:var(--line)}
.nav{top:80px;left:480px;width:660px;height:22px;font-size:16px;color:#444}
.nav span{position:absolute;top:0}
.nav .sep{width:1px;height:22px;background:var(--line)}
.cat-head{left:60px;top:129px;width:222px;height:44px;background:var(--blue);color:#fff;font-weight:700;font-size:16px;padding:13px 18px}
.cat-list{left:60px;top:185px;width:222px;border:1px solid var(--line);border-top:none;list-style:none}
.cat-list li{height:39.6px;border-top:1px solid var(--line);font-size:15px;padding:11px 18px;color:#444}
.cat-list li.active{background:var(--green);color:#fff;border-top:none}
.trust{left:60px;top:808px;width:222px;height:437px;background:#f6f8fb;border:1px solid #e3e8ee;box-shadow:0 0 3px rgba(0,0,0,.08)}
.trust h3{position:absolute;left:12px;top:22px;font-size:15px;font-weight:500;color:#222}
.trust h3 b{color:var(--green);font-weight:400;font-size:22px}
.badge{position:absolute;border-radius:50%;background:#7a7f86}
.badge.gold{background:#d8a52a}
.trust .note{position:absolute;font-size:11px;color:var(--muted);line-height:15px;letter-spacing:.3px}
.trust .accept{position:absolute;left:14px;top:208px;font-size:14px;color:#222}
.pay{position:absolute;font-size:15px;font-weight:500;color:var(--dark);display:flex;align-items:center;justify-content:center;background:#fff;border:1px solid #e0e0e0}
.search{left:305px;top:129px;width:504px;height:48px;border:1px solid var(--line);border-bottom:3px solid #e2e2e2}
.search-btn{position:absolute;left:0;top:0;width:42px;height:45px;background:var(--green)}
.search-ph{position:absolute;left:93px;top:13px;font-size:16px;color:#b9b9b9;font-weight:300}
.cart{left:830px;top:129px;width:310px;height:45px;background:var(--dark);color:#fff;font-size:15px;padding:13px 0 0 66px}
.cart small{font-size:12px}
.hero{left:305px;top:189px;width:835px;height:348px;background:linear-gradient(180deg,#c8d3a0 0%,#6f9a3e 45%,#4e7a2a 100%)}
.dots{position:absolute;right:28px;bottom:19px;display:flex;gap:6px}
.dots i{width:10px;height:10px;border-radius:50%;background:#fff;display:block}
.bar{left:305px;width:835px;height:36px;background:var(--green-pale);border:1px solid #e1ecc8;font-size:17px;font-weight:500;color:var(--green-text);padding:8px 23px}
.card{top:621px;width:264px;height:284px}
.card-img{height:205px}
.card-cap{height:79px;color:#fff;padding:10px 10px;position:relative}
.card-cap h4{font-size:20px;font-weight:500}
.card-cap p{font-size:12px;line-height:18px;margin-top:2px}
.card-cap .go{position:absolute;right:11px;top:46px;width:20px;height:20px;border-radius:50%;background:#fff}
.prod{width:265px}
.prod-img{height:218px;border:1px solid var(--line);position:relative;overflow:hidden;background:#fff}
.prod-photo{position:absolute;left:30px;top:22px;width:190px;height:150px;background:linear-gradient(180deg,#5f8a3b 0%,#6d8f45 40%,#ddd3bb 41%,#cfc4a8 100%);border-radius:6px}
.price{position:absolute;right:0;bottom:0}
.price span{position:absolute;right:2px;bottom:8px;font-size:22px;font-weight:700;color:#fff;white-space:nowrap}
.price small{font-size:13px}
.prod h5{margin-top:13px;font-size:14px;font-weight:400;color:var(--green-text)}
.prod p{margin-top:6px;font-size:12.5px;line-height:18px;color:var(--muted);padding-left:1px;letter-spacing:.3px}
.btn{display:inline-block;margin-top:13px;background:var(--dark);color:#fff;font-size:14px;padding:10px 11px;border-radius:2px}
.footer{left:0;top:1777px;width:1200px;height:211px;background:var(--footer-bg)}
.fcol{position:absolute;top:30px}
.fcol h6{font-size:17px;font-weight:500;color:var(--green-text);margin-bottom:10px}
.fcol li{list-style:none;font-size:12.5px;color:#555;line-height:24px}
.fcol li::before{content:"»  ";color:#777}
.fcol.social li::before{content:none}
.fcol.social li{display:flex;align-items:center;gap:10px;line-height:31px}
.fcol.social i{width:22px;height:22px;border-radius:50%;background:#d5dccd;display:block}
.fcol .info{font-size:12.5px;color:#555;line-height:18px;letter-spacing:.3px}
.fcol .info b{font-weight:500;color:#333}
.bottom{left:0;top:1988px;width:1200px;height:40px;background:var(--green);color:#fff;font-size:12.5px;padding:13px 63px}
.bottom .paym{position:absolute;right:100px;top:9px;display:flex;align-items:center;gap:6px}
.bottom .chip{height:20px;background:#fff;color:var(--dark);font-size:10px;font-weight:500;padding:4px 5px;border-radius:2px}
</style>
</head>
<body>
<div class="page">

  <div class="abs logo">MINARU</div>
  <div class="abs phone">
    <svg width="20" height="24" viewBox="0 0 20 24"><path d="M5 1 L9 6 L6 9 Q8 15 13 18 L16 15 L20 19 L16 23 Q4 20 1 5 Z" fill="#7dbb2c"/></svg>
    +1 0001 4444 5555
  </div>
  <div class="abs currency">Curencies:</div>
  <div class="abs currency-select">US Dollar</div>
  <div class="abs flag" style="left:1083px;background:linear-gradient(#111 33%,#d00 33% 66%,#fc0 66%)"></div>
  <div class="abs flag" style="left:1117px;background:#1d3a8a"></div>
  <div class="abs header-rule"></div>
  <div class="abs nav">
    <span style="left:8px;top:1px"><svg width="24" height="20" viewBox="0 0 24 20"><path d="M12 1 L23 10 H19 V19 H14 V13 H10 V19 H5 V10 H1 Z" fill="#8cc63f"/></svg></span>
    <span class="sep" style="left:57px"></span>
    <span style="left:79px">PRODUCTS</span>
    <span class="sep" style="left:178px"></span>
    <span style="left:194px">SERVICE</span>
    <span class="sep" style="left:274px"></span>
    <span style="left:293px">GARDEN TIPS</span>
    <span class="sep" style="left:411px"></span>
    <span style="left:429px">NEWS</span>
    <span class="sep" style="left:493px"></span>
    <span style="left:513px">Checkout</span>
    <span class="sep" style="left:591px"></span>
    <span style="left:608px">Log In</span>
  </div>

  <div class="abs cat-head">SHOP BY CATEGORY ▾</div>
  <ul class="abs cat-list">
    <li class="active">Seed &amp; Fertilizer</li>
    <li>Handsets</li><li>Manual shears</li><li>Motorized Garden Care</li>
    <li>Lawn Mower</li><li>Expert</li><li>Blue Power</li><li>Lawn</li>
    <li>Grove</li><li>Ground</li><li>Ice &amp; Snow</li><li>Edit</li>
    <li>Maintain</li><li>Mowing</li><li>Electric</li>
  </ul>

  <div class="abs trust">
    <h3>Why Buy From <b>MINARU</b></h3>
    <div class="badge" style="left:20px;top:64px;width:44px;height:44px"></div>
    <div class="note" style="left:72px;top:69px">Secure Shopping<br>Verified Stores certified</div>
    <div class="badge gold" style="left:12px;top:128px;width:60px;height:58px"></div>
    <div class="note" style="left:78px;top:142px">Secure Shopping<br>SSL Certified</div>
    <div class="accept">Also We Accept:</div>
    <div class="pay" style="left:14px;top:232px;width:108px;height:40px">Payluma</div>
    <div class="pay" style="left:132px;top:232px;width:78px;height:40px">Vexa</div>
    <div class="pay" style="left:14px;top:290px;width:50px;height:46px;font-size:11px">Carduna</div>
    <div class="pay" style="left:70px;top:290px;width:66px;height:46px;font-size:11px">Mastrum</div>
    <div class="pay" style="left:144px;top:290px;width:68px;height:46px;font-size:11px">Discora</div>
    <div class="pay" style="left:14px;top:352px;width:196px;height:66px;font-size:20px">Bankflo</div>
  </div>

  <div class="abs search">
    <div class="search-btn"><svg width="42" height="45" viewBox="0 0 42 45"><circle cx="19" cy="20" r="6" fill="none" stroke="#fff" stroke-width="2.5"/><path d="M23.5 24.5 L28 29" stroke="#fff" stroke-width="3"/></svg></div>
    <div class="search-ph">Tell us what you looking....</div>
  </div>
  <div class="abs cart">
    <svg class="abs" style="left:20px;top:10px" width="28" height="24" viewBox="0 0 28 24"><path d="M2 9 H26 L23 22 H5 Z M8 9 L13 2 M20 9 L15 2" fill="none" stroke="#fff" stroke-width="2"/></svg>
    Shopping Cart: <small>0 item(s)</small>
  </div>

  <div class="abs hero" role="img" aria-label="Garden scene with a man pushing a lawn mower and a woman tending flower beds">
    <div class="dots"><i></i><i></i><i></i><i></i><i></i></div>
  </div>

  <div class="abs bar" style="top:562px">TOP PROPDUCTS
    <svg class="abs" style="right:10px;top:12px" width="36" height="12" viewBox="0 0 36 12"><path d="M8 0 L0 6 L8 12 Z M28 0 L36 6 L28 12 Z" fill="#cfd9bd"/></svg>
  </div>
  <div class="abs card" style="left:305px">
    <div class="card-img" role="img" aria-label="Red lawn mower on grass" style="background:linear-gradient(160deg,#5e8c34,#3f6a22 60%,#b8332e)"></div>
    <div class="card-cap" style="background:var(--blue)"><h4>LAWN MOWER</h4><p>Lorem ipsum dolor sit amet,<br>consectetur adipiscing elit. Aliquam</p><span class="go"></span></div>
  </div>
  <div class="abs card" style="left:590px">
    <div class="card-img" role="img" aria-label="Garden trowel and fork in soil" style="background:linear-gradient(180deg,#c7dcea,#9fb9c6 55%,#4c6a2c)"></div>
    <div class="card-cap" style="background:var(--green)"><h4>GARDENING TOOLS</h4><p>Lorem ipsum dolor sit amet,<br>consectetur adipiscing elit. Aliquam</p><span class="go"></span></div>
  </div>
  <div class="abs card" style="left:875px">
    <div class="card-img" role="img" aria-label="String trimmer lying on lawn" style="background:linear-gradient(160deg,#8fc04a,#5f9a2c)"></div>
    <div class="card-cap" style="background:var(--dark)"><h4>STRING TRIMMER</h4><p>Lorem ipsum dolor sit amet,<br>consectetur adipiscing elit. Aliquam</p><span class="go"></span></div>
  </div>

  <div class="abs bar" style="top:942px">FEATURED PRODUCTS</div>

  <div class="abs prod" style="left:305px;top:990px">
    <div class="prod-img"><div class="prod-photo" role="img" aria-label="Wooden raised flower bed with plants"></div>
      <svg class="price" width="88" height="82"><path d="M88 0 V82 H0 Z" fill="#8cc63f"/></svg><div class="price"><span>€34<small>.95</small></span></div></div>
    <h5>Lorem ipsum dolor sit consectetur adipis.</h5>
    <p>Lorem ipsum dolor sit amet conse ctetur adipisicing elit, sed do eiusmod tempor incididunt</p>
    <span class="btn">ADD TO CART</span>
  </div>
  <div class="abs prod" style="left:590px;top:990px">
    <div class="prod-img"><div class="prod-photo" role="img" aria-label="Wooden raised flower bed with plants"></div>
      <svg class="price" width="88" height="82"><path d="M88 0 V82 H0 Z" fill="#8cc63f"/></svg><div class="price"><span>€34<small>.95</small></span></div></div>
    <h5>Lorem ipsum dolor sit consectetur adipis.</h5>
    <p>Lorem ipsum dolor sit amet conse ctetur adipisicing elit, sed do eiusmod tempor incididunt</p>
    <span class="btn">ADD TO CART</span>
  </div>
  <div class="abs prod" style="left:875px;top:990px">
    <div class="prod-img"><div class="prod-photo" role="img" aria-label="Wooden raised flower bed with plants"></div>
      <svg class="price" width="88" height="82"><path d="M88 0 V82 H0 Z" fill="#8cc63f"/></svg><div class="price"><span>€34<small>.95</small></span></div></div>
    <h5>Lorem ipsum dolor sit consectetur adipis.</h5>
    <p>Lorem ipsum dolor sit amet conse ctetur adipisicing elit, sed do eiusmod tempor incididunt</p>
    <span class="btn">ADD TO CART</span>
  </div>
  <div class="abs prod" style="left:305px;top:1380px">
    <div class="prod-img"><div class="prod-photo" role="img" aria-label="Wooden raised flower bed with plants"></div>
      <svg class="price" width="88" height="82"><path d="M88 0 V82 H0 Z" fill="#8cc63f"/></svg><div class="price"><span>€34<small>.95</small></span></div></div>
    <h5>Lorem ipsum dolor sit consectetur adipis.</h5>
    <p>Lorem ipsum dolor sit amet conse ctetur adipisicing elit, sed do eiusmod tempor incididunt</p>
    <span class="btn">ADD TO CART</span>
  </div>
  <div class="abs prod" style="left:590px;top:1380px">
    <div class="prod-img"><div class="prod-photo" role="img" aria-label="Wooden raised flower bed with plants"></div>
      <svg class="price" width="88" height="82"><path d="M88 0 V82 H0 Z" fill="#8cc63f"/></svg><div class="price"><span>€34<small>.95</small></span></div></div>
    <h5>Lorem ipsum dolor sit consectetur adipis.</h5>
    <p>Lorem ipsum dolor sit amet conse ctetur adipisicing elit, sed do eiusmod tempor incididunt</p>
    <span class="btn">ADD TO CART</span>
  </div>
  <div class="abs prod" style="left:875px;top:1380px">
    <div class="prod-img"><div class="prod-photo" role="img" aria-label="Wooden raised flower bed with plants"></div>
      <svg class="price" width="88" height="82"><path d="M88 0 V82 H0 Z" fill="#8cc63f"/></svg><div class="price"><span>€34<small>.95</small></span></div></div>
    <h5>Lorem ipsum dolor sit consectetur adipis.</h5>
    <p>Lorem ipsum dolor sit amet conse ctetur adipisicing elit, sed do eiusmod tempor incididunt</p>
    <span class="btn">ADD TO CART</span>
  </div>

  <div class="abs footer">
    <div class="fcol" style="left:67px"><h6>INFORMATION</h6><ul><li>What's New?</li><li>Products</li><li>About us</li><li>AGB</li><li>Impressum</li></ul></div>
    <div class="fcol" style="left:267px"><h6>WHY BUY FROM US</h6><ul><li>Shipping &amp; Returns</li><li>Secure Shopping</li><li>Top sellers</li><li>Gifts</li><li>Garden Tips</li></ul></div>
    <div class="fcol" style="left:486px"><h6>MY ACCOUNT</h6><ul><li>My Account</li><li>Order History</li><li>Wish List</li><li>Sign in</li><li>Newsletter</li></ul></div>
    <div class="fcol social" style="left:692px"><h6>FOLLOW US</h6><ul><li><i></i>Streamly</li><li><i></i>Friendbook</li><li><i></i>Chirper</li><li><i></i>Vidtube</li></ul></div>
    <div class="fcol" style="left:905px"><h6>CONTACT US</h6>
      <p class="info">comapany address, comapany address<br>comapany address</p>
      <p class="info" style="margin-top:11px">Phone: <b>00041 55210 67</b></p>
      <p class="info" style="margin-top:11px">Support: <b>hallo@minaru.de</b></p>
    </div>
  </div>
  <div class="abs bottom">MINARU © 2013 &nbsp; Privacy Policy &nbsp; | &nbsp;Terms &amp; conditions
    <div class="paym">Payment method: &nbsp;<span class="chip">Payluma</span><span class="chip">Vexa</span><span class="chip">Mastrum</span><span class="chip">girolo</span></div>
  </div>

</div>
</body>
</html>
```